Business Card for Managing Partner Investment Fund

To create a business card template for an investment fund manager. Business card should be more professional in nature, not too colorful, more upscale, and created using the attached logos and fund name files. I would prefer a black or gray color scheme, but am open to the use of color as well. I would prefer a double sided business card, but open to single sided business card designs as well. The business card should include: name, title, and contact information, as well as logo and company name. I would prefer a more stream-lined, simple business card design.
Updates
Address: 4136 NE 19th Ter. Ocala, FL 34470
Email: travis48@quillnet-mail.com
Phone: 561-374-9186
Title: managing partner
Name: Travis Whitlow
Fund Name: Emberfall Capital
Logos can be found in files attached to the brief
Target Market(s)
potential investors, other fund managers
Industry/Entity Type
Finance
Contact Information for Business Card
Name on card: Travis Whitlow
Title: Managing Partner
Font styles to use
Colors
Designer to choose colors to be used in the design.
Requirements
Must have
- Phone number
- email address
- physical address
- title
- name
- logo
- Fund name
Nice to have
- simple layout
Should not have
- too many colors, busy fonts,

```html
<!DOCTYPE html>
<html lang="en">
<head>
<meta charset="utf-8">
<title>Emberfall Capital — Business Card</title>
<link rel="stylesheet" href="https://fonts.googleapis.com/css2?family=Montserrat:wght@400;700&display=swap">
<style>
  :root {
    --stage: #e6e6e6;
    --card-front: #5f5f5f;
    --card-back: #ffffff;
    --ink: #111111;
    --ink-soft: #8a8a8a;
    --rule: #333333;
    --on-dark: #ffffff;
  }
  * { box-sizing: border-box; margin: 0; padding: 0; }
  html, body { width: 1200px; height: 864px; overflow: hidden; }
  body {
    background: var(--stage);
    font-family: "Montserrat", Arial, sans-serif;
    position: relative;
  }
  .card {
    position: absolute;
    left: 337px;
    width: 526px;
    height: 300px;
    border-radius: 22px;
    box-shadow: 0 8px 24px rgba(0,0,0,0.18);
  }
  .card--front { top: 112px; background: var(--card-front); display: flex; align-items: center; justify-content: center; }
  .card--back { top: 452px; background: var(--card-back); }

  .wordmark {
    font-family: "Montserrat", Arial, sans-serif;
    font-weight: 700;
    text-transform: uppercase;
    letter-spacing: 0.06em;
    display: flex;
    align-items: center;
    gap: 10px;
    white-space: nowrap;
  }
  .wordmark__mark { width: 14px; height: 14px; flex: none; }
  .card--front .wordmark { color: var(--on-dark); font-size: 30px; gap: 12px; }
  .card--front .wordmark__mark { background: var(--on-dark); }

  .brand-area {
    position: absolute;
    left: 0;
    top: 0;
    width: 300px;
    height: 100%;
    display: flex;
    align-items: center;
    justify-content: center;
    padding: 0 24px;
  }
  .card--back .wordmark { color: var(--ink); font-size: 16px; padding-top: 40px; }
  .card--back .wordmark__mark { background: var(--ink); width: 10px; height: 10px; }

  .divider {
    position: absolute;
    left: 300px;
    top: 62px;
    width: 1px;
    height: 170px;
    background: var(--rule);
  }
  .contact {
    position: absolute;
    left: 318px;
    top: 66px;
    width: 200px;
  }
  .contact__name { font-size: 17px; font-weight: 700; color: var(--ink); line-height: 1.1; }
  .contact__title { font-size: 11px; color: var(--ink-soft); margin-top: 3px; }
  .contact__address { font-size: 11.5px; color: var(--ink-soft); margin-top: 18px; line-height: 1.4; }
  .contact__lines { list-style: none; margin-top: 14px; }
  .contact__line { display: flex; align-items: center; gap: 6px; font-size: 11px; color: var(--ink-soft); line-height: 1.6; white-space: nowrap; }
  .contact__icon { width: 11px; height: 11px; flex: none; fill: var(--ink); }
</style>
</head>
<body>
  <section class="card card--front" aria-label="Card front">
    <div class="wordmark"><span class="wordmark__mark"></span>Emberfall Capital</div>
  </section>

  <section class="card card--back" aria-label="Card back">
    <div class="brand-area">
      <div class="wordmark"><span class="wordmark__mark"></span>Emberfall Capital</div>
    </div>
    <div class="divider"></div>
    <div class="contact">
      <p class="contact__name">Travis Whitlow</p>
      <p class="contact__title">Managing Partner</p>
      <p class="contact__address">4136 NE 19th Ter. Ocala,<br>FL 34470</p>
      <ul class="contact__lines">
        <li class="contact__line">
          <svg class="contact__icon" viewBox="0 0 24 24" aria-hidden="true"><path d="M6.6 10.8a15.1 15.1 0 0 0 6.6 6.6l2.2-2.2a1 1 0 0 1 1-.25 11.4 11.4 0 0 0 3.6.57 1 1 0 0 1 1 1V20a1 1 0 0 1-1 1A17 17 0 0 1 3 4a1 1 0 0 1 1-1h3.5a1 1 0 0 1 1 1c0 1.25.2 2.45.57 3.57a1 1 0 0 1-.25 1z"/></svg>
          561-374-9186
        </li>
        <li class="contact__line">
          <svg class="contact__icon" viewBox="0 0 24 24" aria-hidden="true"><path d="M2 5h20v14H2z M2 5l10 8 10-8" fill="none" stroke="#111" stroke-width="2"/><path d="M2 5h20L12 13z"/></svg>
          travis48@quillnet-mail.com
        </li>
      </ul>
    </div>
  </section>
</body>
</html>
```